Bramblewood Coatings of Central Florida, LLC. Start-up painting business needs a professional web desig

We have a start up painting business that would like to reach/focus on commercial clients like building contractors, HOA's, apartment complexes, etc.. We would like a residential aspect to the web design as well. We have an existing website at "trybramblewoodcoats.com" with usable content. Have logo and color scheme attached. Use provided website ONLY as template. Add commercial services page. Can type own content when needed.

Industry/Entity Type

Apartment

Number of Pages Required

5+ page

Font styles to use
Serif
Sans Serif
Decorative
Script

Requirements
Must have
• Commercial services

```html
<!DOCTYPE html>
<html lang="en">
<head>
<meta charset="utf-8">
<title>Bramblewood Coatings of Central Florida – Residential Services</title>
<link rel="stylesheet" href="https://fonts.googleapis.com/css2?family=Questrial&family=Montserrat:wght@700&display=swap">
<style>
  :root {
    --wood-light: #e6dccd;
    --wood-light-2: #d4c7b4;
    --wood-warm: #c8652b;
    --wood-deep: #9c4a1c;
    --page: #ffffff;
    --ink: #2b2b2b;
    --olive: #5f6534;
    --peach: #e2a58a;
    --peach-deep: #d98e6e;
    --charcoal: #2f2f2f;
    --yellow: #f2c12e;
    --white: #ffffff;
    --muted: #555555;
  }
  * { margin: 0; padding: 0; box-sizing: border-box; }
  html, body { width: 1200px; height: 2969px; overflow: hidden; }
  body {
    position: relative;
    font-family: "Questrial", "Century Gothic", sans-serif;
    color: var(--ink);
    background: var(--wood-light);
  }
  .backdrop { position: absolute; inset: 0; }
  .abs { position: absolute; }

  /* header */
  .brand {
    left: 40px; top: 40px; display: flex; align-items: center; gap: 12px;
    font-size: 17px; color: var(--ink); width: 260px; line-height: 1.2;
  }
  .brand-mark { width: 40px; height: 40px; border: 3px solid var(--peach-deep); flex: none; }
  .main-nav { left: 300px; top: 0; display: flex; height: 235px; }
  .main-nav a {
    display: flex; align-items: flex-start; justify-content: center; text-align: center;
    padding-top: 106px; font-size: 17px; color: var(--ink); text-decoration: none;
    text-transform: uppercase; line-height: 1.2;
  }
  .nav-home { width: 90px; }
  .nav-about { width: 150px; }
  .nav-residential { width: 136px; background: var(--peach); color: var(--white) !important; }
  .nav-commercial { width: 160px; }
  .nav-contact { width: 190px; }
  .header-phones { left: 905px; top: 14px; font-size: 22px; line-height: 30px; display: flex; gap: 10px; }
  .header-phones svg { margin-top: 6px; }

  /* intro */
  .intro-title { left: 80px; width: 1046px; top: 280px; text-align: center; }
  .intro-title .lead { font-size: 29px; letter-spacing: 0.5px; color: var(--ink); }
  .intro-title .strong {
    font-family: "Montserrat", "Arial", sans-serif; font-weight: 700; font-size: 36px;
    color: var(--olive); letter-spacing: 1px; margin-top: 6px;
  }
  .services-grid {
    left: 148px; top: 438px; width: 896px; height: 566px;
    display: grid; grid-template-columns: repeat(4, 1fr); grid-template-rows: 1fr 1fr; gap: 4px;
    clip-path: polygon(0 0, 100% 0, 100% 97%, 0 100%);
  }
  .grid-photo { width: 100%; height: 100%; }
  .grid-label {
    background: var(--olive); color: var(--white); font-size: 30px; line-height: 1.2;
    padding: 92px 0 0 36px;
  }

  /* services band */
  .services-heading { left: 80px; width: 1046px; top: 1146px; text-align: center; color: var(--peach-deep); font-size: 40px; font-weight: 400; }
  .services-heading::after {
    content: ""; display: block; width: 240px; height: 3px; background: var(--peach-deep); margin: 10px auto 0;
  }
  .services-intro {
    left: 247px; width: 706px; top: 1228px; color: var(--white); font-size: 17px;
    line-height: 1.35; text-align: justify; text-align-last: center;
  }
  .service-circle {
    border-radius: 50%; border: 10px solid var(--peach); color: var(--white);
    display: flex; flex-direction: column; align-items: center; text-align: center; overflow: hidden;
  }
  .service-icon { width: 42px; height: 42px; border-radius: 50%; background: var(--charcoal); display: flex; align-items: center; justify-content: center; flex: none; }
  .service-title { font-size: 28px; line-height: 1.15; text-transform: uppercase; margin-top: 6px; font-weight: 400; }
  .service-title::after { content: ""; display: block; width: 150px; height: 5px; background: var(--yellow); margin: 8px auto 0; }
  .service-text { font-size: 16px; line-height: 1.35; margin-top: 16px; text-align: justify; text-align-last: center; }

  .circle-repair { left: 79px; top: 1398px; width: 460px; height: 460px; padding: 44px 58px 0; background: rgba(120,100,50,0.88); }
  .circle-design { left: 631px; top: 1311px; width: 450px; height: 450px; padding: 24px 50px 0; background: rgba(90,150,150,0.85); }
  .circle-interior { left: 116px; top: 2030px; width: 456px; height: 456px; padding: 48px 62px 0; background: rgba(110,70,70,0.9); }
  .circle-exterior { left: 631px; top: 1962px; width: 456px; height: 456px; padding: 44px 58px 0; background: rgba(120,120,130,0.92); }

  .contact-callout { left: 380px; width: 440px; top: 1866px; text-align: center; }
  .contact-callout .label { color: var(--yellow); font-size: 30px; }
  .contact-callout .phone { color: var(--white); font-size: 30px; line-height: 36px; }

  /* footer */
  .footer-brand { left: 80px; width: 1046px; top: 2494px; text-align: center; color: var(--muted); font-size: 15px; line-height: 1.25; text-transform: uppercase; }
  .footer-brand .footer-mark { width: 74px; height: 74px; border: 4px solid var(--peach-deep); margin: 0 auto 12px; }
  .footer-nav { left: 80px; width: 1046px; top: 2640px; text-align: center; font-size: 13px; text-transform: uppercase; color: var(--ink); }
  .footer-nav span { margin: 0 8px; }
  .footer-social { left: 80px; width: 1046px; top: 2682px; display: flex; justify-content: center; gap: 10px; }
  .footer-social i { display: block; width: 36px; height: 36px; border: 3px solid #7d8fa8; }
  .copyright { left: 0; width: 1200px; top: 2918px; text-align: center; color: var(--white); font-size: 11px; text-transform: uppercase; }
</style>
</head>
<body>
  <svg class="backdrop" width="1200" height="2969" viewBox="0 0 1200 2969">
    <defs>
      <linearGradient id="wood" x1="0" y1="0" x2="0" y2="1">
        <stop offset="0" stop-color="#e9e0d2"/>
        <stop offset="0.35" stop-color="#d9ccb9"/>
        <stop offset="0.48" stop-color="#c66a31"/>
        <stop offset="1" stop-color="#a9511f"/>
      </linearGradient>
      <linearGradient id="teal" x1="0" y1="0" x2="1" y2="0">
        <stop offset="0" stop-color="#6fa3ad"/>
        <stop offset="1" stop-color="#8fb9b8"/>
      </linearGradient>
      <linearGradient id="plum" x1="0" y1="0" x2="1" y2="0">
        <stop offset="0" stop-color="#4a2e3c"/>
        <stop offset="1" stop-color="#5d4a5e"/>
      </linearGradient>
    </defs>
    <rect width="1200" height="2969" fill="url(#wood)" role="img" aria-label="Wooden plank wall background"/>
    <polygon points="80,210 1126,210 1126,2895 86,2906" fill="var(--page)"/>
    <polygon points="80,1125 1126,978 1126,2440 80,2505" fill="var(--charcoal)"/>
    <polygon points="80,1392 1126,1318 1126,1700 80,1845" fill="url(#teal)" role="img" aria-label="Photo of a painter on a ladder in a teal room"/>
    <polygon points="80,2000 1126,1920 1126,2420 80,2490" fill="url(#plum)" role="img" aria-label="Photo of a freshly painted interior at dusk"/>
  </svg>

  <div class="abs brand"><span class="brand-mark"></span><span>Bramblewood Coatings</span></div>

  <nav class="abs main-nav">
    <a class="nav-home" href="#">Home</a>
    <a class="nav-about" href="#">About Us</a>
    <a class="nav-residential" href="#">Residential<br>Services</a>
    <a class="nav-commercial" href="#">Commercial<br>Services</a>
    <a class="nav-contact" href="#">Contact Us</a>
  </nav>

  <div class="abs header-phones">
    <svg width="30" height="30" viewBox="0 0 30 30"><circle cx="15" cy="15" r="13" fill="none" stroke="#2b2b2b" stroke-width="2"/><path d="M10 8 l3 0 l1 4 l-2 1 q2 4 5 5 l1 -2 l4 1 l0 3 q-9 1 -12 -12z" fill="#2b2b2b"/></svg>
    <div>+1.555-640-0132<br>+1.555-944-0117</div>
  </div>

  <header class="abs intro-title">
    <div class="lead">WE OFFER A WIDE VARIETY OF SERVICES</div>
    <div class="strong">TO MEET ALL YOUR NEEDS</div>
  </header>

  <section class="abs services-grid">
    <div class="grid-photo" role="img" aria-label="Photo of a grand warm-toned foyer" style="background:linear-gradient(160deg,#d9a15e,#8a5228)"></div>
    <div class="grid-label">OUR<br>SERVICES</div>
    <div class="grid-photo" role="img" aria-label="Photo of a pink bedroom" style="background:linear-gradient(160deg,#e39ac6,#b54d86)"></div>
    <div class="grid-photo" role="img" aria-label="Photo of a bright green shelving wall" style="background:linear-gradient(160deg,#8fdc48,#3f9a1f)"></div>
    <div class="grid-photo" role="img" aria-label="Photo of a teal hallway with blue doors" style="background:linear-gradient(160deg,#4fa3b0,#2b6e8c)"></div>
    <div class="grid-photo" role="img" aria-label="Photo of a living room with red accents" style="background:linear-gradient(160deg,#f1d5d1,#c0364a)"></div>
    <div class="grid-photo" role="img" aria-label="Photo of an orange media room" style="background:linear-gradient(160deg,#f36b1c,#b9430d)"></div>
    <div class="grid-photo" role="img" aria-label="Photo of a magenta bathroom" style="background:linear-gradient(160deg,#c3215c,#e8e2e2)"></div>
  </section>

  <h2 class="abs services-heading">OUR SERVICES</h2>
  <p class="abs services-intro">We offer a wide variety of services to meet all your needs. When a project comes up no matter planned or unplanned unexpected things can happen. We take the guess work out of the way with our worry free guarantee.</p>

  <article class="abs service-circle circle-design">
    <span class="service-icon"><svg width="22" height="22" viewBox="0 0 22 22"><path d="M3 16 L16 3 M6 19 L19 6 M3 10 L10 3" stroke="#fff" stroke-width="3"/></svg></span>
    <h3 class="service-title">Interior Design<br>Services</h3>
    <p class="service-text">People think painting is the hard part of the job. Try choosing colors with over a millions variations from over 100 manufacturers. The coordination can become overwhelming. We have vast experience with this and can assist you with all your decisions prior to beginning any project.</p>
  </article>

  <article class="abs service-circle circle-repair">
    <span class="service-icon"><svg width="22" height="22" viewBox="0 0 22 22"><path d="M3 16 L16 3 M6 19 L19 6 M3 10 L10 3" stroke="#fff" stroke-width="3"/></svg></span>
    <h3 class="service-title">Repair Services</h3>
    <p class="service-text">No matter what the project you can always bet there will be repairs needed to provide the best job. We provide all minor repairs unlike most competitors who add extra charges as the project progresses. With us you can rest assure the bill we quote is the one you pay!</p>
  </article>

  <div class="abs contact-callout">
    <div class="label">CONTACT US TODAY!</div>
    <div class="phone">+1.555-640-0132</div>
    <div class="phone">+1.555-944-0117</div>
  </div>

  <article class="abs service-circle circle-exterior">
    <span class="service-icon"><svg width="22" height="22" viewBox="0 0 22 22"><path d="M3 16 L16 3 M6 19 L19 6 M3 10 L10 3" stroke="#fff" stroke-width="3"/></svg></span>
    <h3 class="service-title">Exterior Painting<br>Services</h3>
    <p class="service-text">When it comes to painting your homes exterior is can seem like an overwhelming endeavor. We have all the tools to make any exterior project look easy.</p>
  </article>

  <article class="abs service-circle circle-interior">
    <span class="service-icon"><svg width="22" height="22" viewBox="0 0 22 22"><path d="M3 16 L16 3 M6 19 L19 6 M3 10 L10 3" stroke="#fff" stroke-width="3"/></svg></span>
    <h3 class="service-title">Interior Painting<br>Services</h3>
    <p class="service-text">Sometimes just a coat of paint is all you may need for a fresh look. Other times you need a little more. With our huge line of interior painting services there isn't a job to big or small we can't preform.</p>
  </article>

  <footer>
    <div class="abs footer-brand"><div class="footer-mark"></div>Bramblewood Coatings of<br>Central Florida, LLC.</div>
    <div class="abs footer-nav">Home<span>|</span>About Us<span>|</span>Services<span>|</span>Commercial Services<span>|</span>Contact Us</div>
    <div class="abs footer-social"><i></i><i></i><i></i><i></i></div>
    <div class="abs copyright">Copyright © Bramblewood Coatings. All rights reserved.</div>
  </footer>
</body>
</html>
```